Pals of Rusty Fundraiser Flyer for shelter dogs

Flyer for Fund Raiser for shelter and rescue dogsThis will be hosted by who we are calling Heroes First responders (Fire, Police, and EMS will be bartending raising money to help the shelter dogs).

I will be uploading a basic flyer I did but I don't like it, only showing for dates and words etc...

struggling to come up with something eye-catching related to the above.

We can keep the use of Heroes (spelled wrong on the flyer)but open for new ideas too and new title.

Target Market(s)

Animal lovers

Font styles to use
Serif
Sans Serif

Requirements
Must have
• the ties to first responders and dog rescue
• Must include First responder logo badges images. The image with the helping hands Maybe replace the badges with images of dogs or doggy paws something like that
• Must have a strong presence identifying and relating to first responders
• Images of first responders as well as even images of the first responder logos for fire department police department and EMS.
• The first responders are the ones hosting the event so we really want to raise them up and show their appreciation for the cause that is super important as well
• Title should read
• Guardians Guarding Mutts

```html
<!DOCTYPE html>
<html lang="en">
<head>
<meta charset="utf-8">
<title>Pals of Rusty – Guardians Guarding Mutts</title>
<link rel="stylesheet" href="https://fonts.googleapis.com/css2?family=Oswald:wght@700&family=Roboto:wght@700&display=swap">
<style>
  :root {
    --backdrop: #000000;
    --paper: #ffffff;
    --red: #e30f13;
    --red-deep: #7a1f22;
    --gold: #a36b30;
    --text-light: #ffffff;
  }
  * { margin: 0; padding: 0; box-sizing: border-box; }
  html, body { width: 927px; height: 1200px; overflow: hidden; background: var(--backdrop); }
  body { position: relative; font-family: "Roboto", Arial, sans-serif; font-weight: 700; }

  .flyer {
    position: absolute; left: 95px; top: 122px; width: 739px; height: 956px;
    background: var(--paper); overflow: hidden;
  }
  .flyer__top-rule { position: absolute; left: 0; top: 0; width: 100%; height: 7px; background: var(--gold); }
  .flyer__wave { position: absolute; left: 0; top: 540px; width: 739px; height: 416px; }

  .hero-art {
    position: absolute; left: 45px; top: 60px; width: 330px; height: 330px;
    background: linear-gradient(160deg, var(--red) 0%, var(--red) 62%, var(--gold) 63%, var(--gold) 100%);
    border-radius: 48% 48% 40% 40%;
  }

  .brand {
    position: absolute; left: 545px; top: 42px; width: 170px; text-align: center; color: var(--red);
    font-size: 17px; line-height: 1.15;
  }
  .brand__dot { display: block; width: 74px; height: 74px; margin: 0 auto 8px; border-radius: 50%; background: var(--red); }
  .brand__sub { display: block; font-size: 9px; margin-top: 3px; }

  .title { position: absolute; left: 0; top: 300px; width: 739px; height: 230px; }
  .title text { font-family: "Oswald", "Arial Narrow", sans-serif; font-weight: 700; }
  .title__line1 { fill: var(--red); }
  .title__line2 { fill: var(--gold); }

  .details { position: absolute; inset: 0; color: var(--text-light); text-align: center; }
  .details > * { position: absolute; left: 0; width: 100%; }
  .details__intro { top: 611px; font-size: 15.5px; line-height: 23px; }
  .details__rule { left: 180px; width: 378px; height: 5px; background: var(--gold); }
  .details__rule--upper { top: 722px; }
  .details__rule--lower { top: 849px; }
  .details__date { top: 738px; font-size: 25px; line-height: 26px; }
  .details__time { top: 765px; font-size: 25px; line-height: 26px; }
  .details__hosted { top: 789px; font-size: 11px; line-height: 14px; }
  .details__venue { top: 806px; font-size: 29px; line-height: 34px; }

  .contacts { top: 871px; list-style: none; font-size: 12.5px; line-height: 21.5px; }
  .contacts__mark { display: inline-block; width: 9px; height: 9px; background: var(--text-light); margin-right: 8px; vertical-align: -1px; }
  .contacts__globe { display: inline-block; width: 10px; height: 10px; margin-right: 8px; vertical-align: -1px; }
</style>
</head>
<body>
  <main class="flyer">
    <div class="flyer__top-rule"></div>

    <div class="hero-art" role="img" aria-label="Illustration of a red dog paw print framing silhouettes of a paramedic, firefighter and police officer, cradled by an open gold hand"></div>

    <div class="brand">
      <span class="brand__dot"></span>
      Pals of Rusty
      <span class="brand__sub">Ridgewater County Dog Pound</span>
    </div>

    <svg class="title" viewBox="0 0 739 230" aria-label="Guardians Guarding Mutts">
      <text class="title__line1" x="400" y="118" font-size="124" textLength="275" lengthAdjust="spacingAndGlyphs">GUARDIANS</text>
      <text class="title__line2" x="123" y="218" font-size="124" textLength="567" lengthAdjust="spacingAndGlyphs">GUARDING MUTTS</text>
    </svg>

    <svg class="flyer__wave" viewBox="0 0 739 416" preserveAspectRatio="none" aria-hidden="true">
      <defs>
        <linearGradient id="waveFill" x1="0" y1="0" x2="0" y2="1">
          <stop offset="0" stop-color="#e30f13"/>
          <stop offset="1" stop-color="#7a1f22"/>
        </linearGradient>
      </defs>
      <path d="M0 45 C120 20 250 0 370 6 C500 12 620 40 739 55 L739 416 L0 416 Z" fill="url(#waveFill)"/>
    </svg>

    <section class="details">
      <p class="details__intro">
        Join Pals of Rusty for an evening of fun!<br>
        Come spend an evening with our Celebrity Bartenders and help<br>
        some pups in need. Our local men and women<br>
        in uniform will be pouring drinks and raising awareness of adoption.
      </p>
      <div class="details__rule details__rule--upper"></div>
      <p class="details__date">AUG 15, 2019</p>
      <p class="details__time">6-10 PM</p>
      <p class="details__hosted">Hosted at</p>
      <p class="details__venue">The Harbor Room</p>
      <div class="details__rule details__rule--lower"></div>
      <ul class="contacts">
        <li><span class="contacts__mark"></span>Social@palsofrustyrcdp</li>
        <li><span class="contacts__mark"></span>Feed@porcdp</li>
        <li><svg class="contacts__globe" viewBox="0 0 10 10" aria-hidden="true"><g fill="none" stroke="#ffffff" stroke-width="1"><circle cx="5" cy="5" r="4.4"/><ellipse cx="5" cy="5" rx="2" ry="4.4"/><line x1="0.6" y1="5" x2="9.4" y2="5"/></g></svg>www.palsofrustyridgewater.org</li>
      </ul>
    </section>
  </main>
</body>
</html>
```